New business card design needed for Trucking/Staffing company!

I am looking for a business card design. The business name is Harbor Lane Freightworks, LLC. This company is a staffing company for commercial drivers/truck drivers. Most of our customers are trucking/supply companies. Our colors are blue/black/white/grey. The info I have on my current business cards is
-Spot for a name
-2 lines for an address
-3 lines for Office, cell, and fax
-email
-website(currently on backside of card with logo but can go anywhere)
Updates

Project Deadline Extended
Reason: Open to more designs

Target Market(s)

Trucking companies, building supply companies

Industry/Entity Type

Business

Contact Information for Business Card

Edgy but professional

Font styles to use
Other font styles liked:
• Open to suggestions

Colors
0555a3
000000
ffffff
9d9d9d

Requirements
Must have
• Must have the logo incorporated

```html
<!DOCTYPE html>
<html lang="en">
<head>
<meta charset="utf-8">
<title>Harbor Lane Freightworks – Business Card</title>
<link href="https://fonts.googleapis.com/css2?family=Open+Sans:wght@400;600;700&display=swap" rel="stylesheet">
<style>
  :root {
    --blue: #2b3591;
    --black: #000000;
    --white: #ffffff;
    --grey: #c9c9c9;
    --grey-dark: #9d9d9d;
    --backdrop: #d9d9d9;
  }
  html, body {
    margin: 0;
    padding: 0;
    width: 1200px;
    height: 900px;
    overflow: hidden;
    background: var(--backdrop);
    font-family: "Open Sans", Arial, sans-serif;
  }
  .canvas {
    position: relative;
    width: 1200px;
    height: 900px;
  }
  .card {
    position: absolute;
    width: 600px;
    height: 343px;
    overflow: hidden;
    box-shadow: 0 6px 18px rgba(0,0,0,0.18);
  }
  .card--back {
    left: 440px;
    top: 70px;
    background: var(--blue);
    display: flex;
    align-items: center;
    justify-content: center;
  }
  .card--front {
    left: 160px;
    top: 470px;
    background: var(--blue);
  }
  .card__art {
    position: absolute;
    inset: 0;
    width: 100%;
    height: 100%;
  }
  .brand {
    display: flex;
    align-items: center;
    gap: 12px;
    color: var(--white);
    font-weight: 700;
    font-size: 26px;
    letter-spacing: 1px;
    text-transform: uppercase;
    white-space: nowrap;
  }
  .brand__mark {
    width: 18px;
    height: 18px;
    background: var(--white);
  }
  .card--front .brand {
    position: absolute;
    left: 170px;
    top: 78px;
    font-size: 22px;
  }
  .card--front .brand__mark {
    width: 16px;
    height: 16px;
  }
  .holder {
    position: absolute;
    left: 38px;
    top: 214px;
    color: var(--white);
  }
  .holder__name {
    margin: 0 0 10px;
    font-size: 20px;
    font-weight: 700;
  }
  .holder__address {
    margin: 0;
    font-size: 15px;
    line-height: 1.35;
    font-style: normal;
  }
  .contact {
    position: absolute;
    right: 30px;
    top: 206px;
    margin: 0;
    padding: 0;
    list-style: none;
    color: var(--white);
    font-size: 16px;
    line-height: 1;
  }
  .contact__item {
    display: flex;
    justify-content: flex-end;
    align-items: center;
    gap: 10px;
    height: 24px;
  }
  .contact__icon {
    width: 14px;
    height: 14px;
    fill: var(--white);
    stroke: none;
  }
</style>
</head>
<body>
<main class="canvas">

  <section class="card card--back" aria-label="Card back">
    <div class="brand"><span class="brand__mark"></span>Harbor Lane Freightworks</div>
  </section>

  <section class="card card--front" aria-label="Card front">
    <svg class="card__art" viewBox="0 0 600 343" preserveAspectRatio="none" aria-hidden="true">
      <path d="M0 0 H600 V130 C420 220 150 200 0 60 Z" fill="var(--black)"/>
      <path d="M0 60 C150 200 420 220 600 130 V140 C420 232 140 216 0 84 Z" fill="var(--grey)"/>
      <path d="M0 84 C140 216 420 232 600 140 V145 C420 238 140 222 0 90 Z" fill="var(--black)"/>
    </svg>

    <div class="brand"><span class="brand__mark"></span>Harbor Lane Freightworks</div>

    <div class="holder">
      <h1 class="holder__name">Daniel Reyes</h1>
      <address class="holder__address">12345, Address Goes Here<br>Country Name, 123456.</address>
    </div>

    <ul class="contact">
      <li class="contact__item">044-456-7890
        <svg class="contact__icon" viewBox="0 0 16 16"><path d="M3 1h3l1.5 4-2 1.3a9 9 0 0 0 4.2 4.2L11 8.5l4 1.5v3a2 2 0 0 1-2 2C6.4 15 1 9.6 1 3a2 2 0 0 1 2-2z"/></svg>
      </li>
      <li class="contact__item">123-456-7890
        <svg class="contact__icon" viewBox="0 0 16 16"><path d="M1 5c2-3 12-3 14 0v2h-4V5H5v2H1z"/><rect x="3" y="8" width="10" height="6" rx="1"/></svg>
      </li>
      <li class="contact__item">123-456-7890
        <svg class="contact__icon" viewBox="0 0 16 16"><rect x="4" y="1" width="8" height="5"/><rect x="2" y="6" width="12" height="9" rx="1"/></svg>
      </li>
      <li class="contact__item">info@youremail.com
        <svg class="contact__icon" viewBox="0 0 16 16"><path d="M1 3h14v10H1z M1 3l7 6 7-6" stroke="var(--blue)" stroke-width="1.2"/></svg>
      </li>
      <li class="contact__item">www.website.com
        <svg class="contact__icon" viewBox="0 0 16 16"><circle cx="8" cy="8" r="7"/><path d="M1 8h14M8 1c-3 4-3 10 0 14M8 1c3 4 3 10 0 14" stroke="var(--blue)" stroke-width="1" fill="none"/></svg>
      </li>
    </ul>
  </section>

</main>
</body>
</html>
```